Brovanta Energy Ratings Whole Home Energy Rating Flyer

Please create a flyer 8.5" x 11" that is 2-sided that goes hand and hand with my tri-fold flyer. The flyer will target prospective homeowners and real estate agents to purchase a whole home energy rating. I have attached further details.

Target Market(s)

Homeowners looking to remodel their homes, save on energy bills, purchase or sell a home.

Font styles to use
Serif
Sans Serif

Colors
3176b5
ffffff

Requirements
Must have
• Must be able to sell a whole home energy rating on its own!
Nice to have
• I would like to mimic the colors and background of my tri-fold flyer.
Should not have
• Should not be boring!

```html
<!DOCTYPE html>
<html lang="en">
<head>
<meta charset="utf-8">
<title>Brovanta Energy Ratings – Whole Home Energy Rating</title>
<link rel="stylesheet" href="https://fonts.googleapis.com/css2?family=Jost:wght@400;500;600;700&display=swap">
<style>
  :root {
    --brand-blue: #3176b5;
    --deep-blue: #2a5fa8;
    --navy: #0d1b2e;
    --sky: #a6dcda;
    --pale-blue: #c4e6f7;
    --window-blue: #b9e0f6;
    --lime: #cfdf4a;
    --teal: #1d8d9a;
    --ink: #1c1c1c;
    --white: #ffffff;
  }
  * { box-sizing: border-box; margin: 0; padding: 0; }
  html, body { width: 1200px; height: 933px; overflow: hidden; }
  body { font-family: "Jost", sans-serif; color: var(--ink); }
  .flyer {
    position: relative; width: 1200px; height: 933px; overflow: hidden;
    background: linear-gradient(180deg, var(--sky) 0%, #d7efef 28%, var(--white) 55%, var(--white) 100%);
  }
  .decor { position: absolute; inset: 0; width: 1200px; height: 933px; }
  .brand {
    position: absolute; left: 26px; top: 56px;
    display: flex; align-items: center; gap: 9px;
    font-weight: 700; font-size: 25px; color: var(--navy); letter-spacing: .3px;
  }
  .brand-square { width: 16px; height: 16px; background: var(--brand-blue); }
  .column { position: absolute; top: 146px; font-size: 15.2px; line-height: 27px; }
  .column h2 { font-size: 15.4px; font-weight: 600; color: var(--brand-blue); line-height: 27px; white-space: nowrap; }
  .col-intro { left: 25px; width: 370px; }
  .col-who { left: 418px; width: 370px; }
  .col-rater { left: 831px; width: 350px; }
  .lead { color: var(--brand-blue); font-weight: 600; }
  .l { display: block; white-space: nowrap; }
  .section-gap { margin-top: 27px; }
  .checks { list-style: none; }
  .checks li { display: flex; align-items: center; gap: 5px; white-space: nowrap; }
  .tick { width: 15px; height: 15px; flex: none; }
  .checks-grid { position: absolute; left: 829px; top: 740px; display: grid; grid-template-columns: 147px 150px; font-size: 15.2px; line-height: 27px; list-style: none; }
  .checks-grid li { display: flex; align-items: center; gap: 5px; white-space: nowrap; }
  .house-diagram {
    position: absolute; left: 861px; top: 524px; width: 264px; height: 205px;
    background: linear-gradient(180deg, #6fb4da 0%, #3a6f9c 55%, #1b1d1f 100%);
  }
  .solar-photo {
    position: absolute; left: 0; top: 680px; width: 485px; height: 253px;
    background: linear-gradient(160deg, #9fb4d6 0%, #4c6ea6 45%, #2b3f6a 100%);
    clip-path: polygon(0 0, 30% 30%, 62% 68%, 100% 100%, 0 100%);
  }
</style>
</head>
<body>
<main class="flyer">
  <svg class="decor" viewBox="0 0 1200 933" aria-hidden="true">
    <polygon points="0,0 170,0 330,58 352,55 399,93 399,113 250,82 50,88 0,70" fill="var(--brand-blue)"/>
    <polygon points="399,93 457,137 399,113" fill="var(--lime)"/>
    <polygon points="799,322 399,634 799,469" fill="var(--lime)"/>
    <polygon points="368,832 646,687 1018,857 960,933 368,933" fill="var(--pale-blue)" opacity=".8"/>
    <polygon points="0,590 90,650 170,700 260,770 390,933 0,933" fill="var(--brand-blue)"/>
    <g fill="var(--window-blue)">
      <rect x="735" y="786" width="25" height="30"/><rect x="772" y="786" width="25" height="30"/>
      <rect x="735" y="827" width="25" height="30"/><rect x="772" y="827" width="25" height="30"/>
    </g>
    <path d="M700,933 C900,905 1100,840 1200,760 L1200,933 Z" fill="var(--deep-blue)"/>
    <path d="M780,933 C950,915 1110,860 1200,800 L1200,933 Z" fill="var(--lime)"/>
    <path d="M840,933 C990,922 1130,880 1200,835 L1200,933 Z" fill="var(--teal)"/>
    <path d="M940,933 C1050,925 1150,895 1200,870 L1200,933 Z" fill="var(--deep-blue)"/>
  </svg>

  <div class="solar-photo" role="img" aria-label="Photograph of a tiled house roof covered with solar panels"></div>

  <header class="brand"><span class="brand-square"></span>Brovanta Energy Ratings</header>

  <section class="column col-intro">
    <p>
      <span class="l"><span class="lead">Would you like to</span> lower your monthly energy bill,</span>
      <span class="l">enjoy a safer, more comfortable and durable home,</span>
      <span class="l">increase your homes appraisal value and sales</span>
      <span class="l">appeal?! Then keep reading, because</span>
      <span class="l">that is what a lost cost, home energy rating can do for</span>
      <span class="l">you…</span>
    </p>
    <h2 class="section-gap">What is a Whole Home Energy Rating?</h2>
    <p>
      <span class="l">A Whole Home Energy Rating is a comprehensive</span>
      <span class="l">evaluation of the efficiency of the entire home. You will</span>
      <span class="l">receive a written report that includes a numeric score</span>
      <span class="l">or “rating” of the home, plus recommendations for</span>
      <span class="l">improvements that will reduce energy bills and make</span>
      <span class="l">the home more comfortable. Each rating will receive</span>
      <span class="l">an official Westland Home Energy Rating Certificate</span>
      <span class="l">and home energy rating report with the Westland</span>
      <span class="l">Energy Board’s (WEB) seal. The report will</span>
      <span class="l" style="padding-left:22px">dentify the most cost-effective and appropriate</span>
      <span class="l" style="padding-left:61px">energy efficiency improvements needed to</span>
      <span class="l" style="padding-left:96px">save your money and provide long</span>
      <span class="l" style="padding-left:136px">lasting comfort</span>
    </p>
  </section>

  <section class="column col-who">
    <h2>Who needs a Whole Home Energy Rating?</h2>
    <p>
      <span class="l">Everyone! Whether you are buying or selling, or plan</span>
      <span class="l">on staying in your home for one year or the rest of</span>
      <span class="l">your life, each whole home energy rating is geared</span>
      <span class="l">toward helping you save money, and is custom</span>
      <span class="l">tailored to fit your unique needs. The whole home</span>
      <span class="l">energy rating can be designed to fit any lifestyle or</span>
      <span class="l">energy improvement budget, with a focal point on</span>
      <span class="l">cost effectiveness and common sense.</span>
      <span class="l">Buyers who choose to get a whole home energy</span>
      <span class="l">rating can better decide which home will save them</span>
      <span class="l">money through energy efficiency! They may also be</span>
      <span class="l">entitled to federal tax credits, and borrow up to</span>
      <span class="l">$40,000 for energy improvements through their</span>
      <span class="l">mortgage.</span>
      <span class="l">Sellers who have a WEB certificate showing their</span>
      <span class="l">homes energy efficiency ultimately make their homes</span>
      <span class="l">more valuable and often sell their homes faster than</span>
      <span class="l">those without documentation.</span>
      <span class="l">Before you remodel your home, make sure you have</span>
      <span class="l">a HESS Rater conduct a Whole Home Energy Rating</span>
      <span class="l">so you know exactly where to focus your money.</span>
    </p>
  </section>

  <section class="column col-rater">
    <h2>Who performs the rating?</h2>
    <p>
      <span class="l">A Home Energy Scoring Standard (HESS) Rater,</span>
      <span class="l">certified by the WEB, will conduct the rating. Each</span>
      <span class="l">Westland HESS Rater must follow standardized</span>
      <span class="l">energy auditing procedures and use energy analysis</span>
      <span class="l">software that meets WEB requirements.</span>
      <span class="l">The HESS Rater will inspect and assess all the major</span>
      <span class="l">energy efficiency features of your home:</span>
    </p>
    <ul class="checks">
      <li><svg class="tick" viewBox="0 0 16 16"><path d="M1 9l4 5L15 2" fill="none" stroke="#000" stroke-width="3"/></svg>Air leaks</li>
      <li><svg class="tick" viewBox="0 0 16 16"><path d="M1 9l4 5L15 2" fill="none" stroke="#000" stroke-width="3"/></svg>Cooling system</li>
      <li><svg class="tick" viewBox="0 0 16 16"><path d="M1 9l4 5L15 2" fill="none" stroke="#000" stroke-width="3"/></svg>Heating system</li>
      <li><svg class="tick" viewBox="0 0 16 16"><path d="M1 9l4 5L15 2" fill="none" stroke="#000" stroke-width="3"/></svg>Cooling/heating duct system</li>
      <li><svg class="tick" viewBox="0 0 16 16"><path d="M1 9l4 5L15 2" fill="none" stroke="#000" stroke-width="3"/></svg>Water heating system</li>
      <li><svg class="tick" viewBox="0 0 16 16"><path d="M1 9l4 5L15 2" fill="none" stroke="#000" stroke-width="3"/></svg>Insulation (attic, walls, floor, roof)</li>
    </ul>
  </section>

  <div class="house-diagram" role="img" aria-label="Cutaway illustration of a house showing where air leaks into and out of the home"></div>

  <ul class="checks-grid">
    <li><svg class="tick" viewBox="0 0 16 16"><path d="M1 9l4 5L15 2" fill="none" stroke="#000" stroke-width="3"/></svg>Windows</li>
    <li><svg class="tick" viewBox="0 0 16 16"><path d="M1 9l4 5L15 2" fill="none" stroke="#000" stroke-width="3"/></svg>Lighting</li>
    <li><svg class="tick" viewBox="0 0 16 16"><path d="M1 9l4 5L15 2" fill="none" stroke="#000" stroke-width="3"/></svg>Major appliances</li>
    <li><svg class="tick" viewBox="0 0 16 16"><path d="M1 9l4 5L15 2" fill="none" stroke="#000" stroke-width="3"/></svg>Solar (if any)</li>
    <li><svg class="tick" viewBox="0 0 16 16"><path d="M1 9l4 5L15 2" fill="none" stroke="#000" stroke-width="3"/></svg>Other energy uses</li>
    <li><svg class="tick" viewBox="0 0 16 16"><path d="M1 9l4 5L15 2" fill="none" stroke="#000" stroke-width="3"/></svg>Prior energy bills</li>
  </ul>
</main>
</body>
</html>
```